Business IT Services Billboard to attract local small businesses

We are Brivolane, a premier Managed Service Provider (MSP) specializing in comprehensive IT services and VOIP phone solutions exclusively for businesses. Our goal is to create a dynamic and visually engaging billboard advertisement that not only highlights our cutting-edge IT solutions but also emphasizes our state-of-the-art VOIP phone services. This billboard should communicate our commitment to providing innovative, reliable, and holistic technology solutions.
Target Market(s)
small business
Industry/Entity Type
Information Technology
Colors
Designer to choose colors to be used in the design.
Look and feel
Each slider illustrates characteristics of the customer's brand and the style your logo design should communicate.

```html
<!DOCTYPE html>
<html lang="en">
<head>
<meta charset="utf-8">
<title>Brivolane Billboard</title>
<link href="https://fonts.googleapis.com/css2?family=Roboto:wght@300;400;700&family=Roboto+Condensed:wght@400;700&display=swap" rel="stylesheet">
<style>
  :root {
    --page-bg: #e3e3e3;
    --board-white: #ffffff;
    --brand-blue: #0e6fbd;
    --ink: #1f1f1f;
    --swoosh-grey: #b9bcc0;
    --tint-blue: #d7eaf8;
    --photo-dark: #2b2f33;
  }
  * { margin: 0; padding: 0; box-sizing: border-box; }
  html, body {
    width: 1071px;
    height: 1200px;
    overflow: hidden;
    background: var(--page-bg);
  }
  .billboard {
    position: absolute;
    left: 30px;
    top: 379px;
    width: 1011px;
    height: 442px;
    overflow: hidden;
    background: linear-gradient(100deg, var(--tint-blue) 0%, #eef6fc 40%, var(--board-white) 70%);
    box-shadow: 0 8px 18px rgba(0, 0, 0, 0.12);
  }
  .swoosh {
    position: absolute;
    left: 0;
    top: 0;
    width: 1011px;
    height: 442px;
  }
  .brand-name {
    position: absolute;
    left: 52px;
    top: 26px;
    font-family: "Roboto", sans-serif;
    font-weight: 700;
    font-size: 56px;
    letter-spacing: 2px;
    line-height: 1;
    color: var(--brand-blue);
  }
  .call-to-action {
    position: absolute;
    right: 51px;
    top: 34px;
    text-align: right;
  }
  .call-to-action .lead {
    font-family: "Roboto", sans-serif;
    font-weight: 300;
    font-size: 17px;
    color: var(--ink);
    line-height: 1.1;
  }
  .call-to-action .web-address {
    font-family: "Roboto Condensed", sans-serif;
    font-weight: 400;
    font-size: 25px;
    color: var(--brand-blue);
    line-height: 1.05;
  }
  .product-visual {
    position: absolute;
    left: 48px;
    top: 178px;
    width: 410px;
    height: 250px;
    border-radius: 6px;
    background: radial-gradient(ellipse at 60% 55%, var(--photo-dark) 0%, #5a6570 45%, rgba(120, 170, 215, 0.35) 75%, rgba(215, 234, 248, 0) 100%);
  }
  .headline {
    position: absolute;
    left: 466px;
    top: 204px;
    font-family: "Roboto", sans-serif;
    font-weight: 300;
    font-size: 49px;
    line-height: 46px;
    color: var(--ink);
    white-space: nowrap;
  }
  .headline .accent {
    font-family: "Roboto Condensed", sans-serif;
    font-weight: 700;
    color: var(--brand-blue);
  }
  .subline {
    position: absolute;
    left: 467px;
    top: 362px;
    font-family: "Roboto Condensed", sans-serif;
    font-weight: 400;
    font-size: 20px;
    line-height: 26px;
    color: var(--ink);
  }
</style>
</head>
<body>
  <section class="billboard">
    <svg class="swoosh" viewBox="0 0 1011 442" aria-hidden="true">
      <path d="M0,80 C40,135 160,150 330,140 C560,126 800,105 1011,125 L1011,135 C800,120 560,150 330,168 C170,180 50,178 0,170 Z" fill="var(--swoosh-grey)" opacity="0.7"/>
      <path d="M0,62 C30,108 150,120 320,112 C560,100 820,80 1011,112 L1011,125 C800,100 560,122 330,140 C160,152 40,150 0,140 Z" fill="var(--brand-blue)"/>
    </svg>

    <div class="brand-name">Brivolane</div>

    <div class="call-to-action">
      <p class="lead">Transform Your Tech Today at</p>
      <p class="web-address">www.brivolane.com</p>
    </div>

    <div class="product-visual" role="img" aria-label="Desk VOIP phone photo with hexagon service icons for chart, wifi, team, network and email"></div>

    <h1 class="headline">Elevate Your Business<br>with <span class="accent">Next-Gen IT</span> and<br><span class="accent">VOIP Services</span></h1>

    <p class="subline">Innovative&nbsp; IT and VOIP Solutions<br>Tailored for Your Business Success.</p>
  </section>
</body>
</html>
```